Marvia Quenby Business Cards

We Need two Business Cards with bleeds. the only difference between the two cards is the backaround color one lilac and pink. Attached we have the cards please match up the logo's and text. Take out the orange box out.

Target Market(s)

double-sided business cards

Industry/Entity Type

Business

Logo Text

match up as best as possible

Colors
f59195
d2a4cc

Requirements
Must have
• n/a
Nice to have
• n/a
Should not have
• n/a

```html
<!DOCTYPE html>
<html lang="en">
<head>
<meta charset="utf-8">
<title>Marvia Quenby-Hollis MD Business Cards</title>
<link rel="stylesheet" href="https://fonts.googleapis.com/css2?family=Arimo:wght@400;700&family=Tinos&family=Pinyon+Script&display=swap">
<style>
  :root {
    --lilac: #d2a4cc;
    --pink: #f59195;
    --ink: #111111;
    --name-fill: #c46a66;
    --name-stroke: #3a2020;
    --circle-gold: #d4b048;
    --page: #ffffff;
  }
  html, body {
    margin: 0;
    width: 1200px;
    height: 742px;
    overflow: hidden;
    background: var(--page);
  }
  .sheet {
    position: relative;
    width: 1200px;
    height: 742px;
  }
  .card {
    position: absolute;
    width: 562px;
    height: 321px;
    background: var(--card-bg);
    color: var(--ink);
    overflow: hidden;
  }
  .card--lilac { --card-bg: var(--lilac); top: 37px; }
  .card--pink  { --card-bg: var(--pink);  top: 376px; }
  .card--front { left: 27px; font-family: "Arimo", Arial, sans-serif; }
  .card--back  { left: 609px; font-family: "Tinos", "Times New Roman", serif; }

  .line {
    position: absolute;
    margin: 0;
    line-height: 1;
    font-weight: 400;
    white-space: nowrap;
    transform: translateY(-50%);
  }
  .centered { left: 0; right: 0; text-align: center; }

  /* Front */
  .front-name {
    top: 47px;
    font-size: 33px;
    font-weight: 700;
    color: var(--name-fill);
    -webkit-text-stroke: 1.2px var(--name-stroke);
  }
  .front-cert { top: 81px; font-size: 24px; }
  .front-specialty { top: 121px; font-size: 24px; }
  .front-appointment { top: 144px; right: 55px; font-size: 17px; }
  .front-mark { position: absolute; left: 23px; top: 138px; }
  .front-services {
    position: absolute;
    left: 144px;
    top: 160px;
    margin: 0;
    padding: 0;
    list-style: none;
    font-size: 20px;
    line-height: 19.5px;
  }
  .front-address { top: 259px; font-size: 15.5px; }
  .front-contact { top: 280px; font-size: 15.5px; }
  .front-contact span + span { margin-left: 14px; }

  /* Back */
  .back-name { top: 38px; font-size: 26px; }
  .back-cert { top: 67px; font-size: 26px; }
  .back-specialty {
    top: 99px;
    left: 87px;
    width: 391px;
    font-size: 22px;
    border-bottom: 1.5px solid var(--ink);
    padding-bottom: 1px;
  }
  .back-specialty .script {
    font-family: "Pinyon Script", cursive;
    font-size: 25px;
  }
  .back-mark { position: absolute; left: 12px; top: 102px; }
  .back-service { font-size: 21px; }
  .back-detail { left: 289px; font-size: 18.5px; }
  .back-phone { left: 289px; font-size: 21px; letter-spacing: 0.5px; }
  .back-email { left: 289px; font-size: 17px; }
  .back-appointment { top: 286px; left: 13px; font-size: 16px; }
</style>
</head>
<body>
<main class="sheet">

  <section class="card card--front card--lilac" aria-label="Business card front, lilac">
    <h1 class="line centered front-name">Marvia Quenby-Hollis MD</h1>
    <p class="line centered front-cert">Board Certified</p>
    <p class="line centered front-specialty">Women's Health &amp; Wellness Specialist</p>
    <p class="line front-appointment">By Appointment</p>
    <svg class="front-mark" width="116" height="100" viewBox="0 0 116 100" aria-hidden="true">
      <circle cx="58" cy="62" r="37" fill="var(--circle-gold)"/>
    </svg>
    <ul class="front-services">
      <li>Obstetrics</li>
      <li>Gynecology</li>
      <li>Family Planning</li>
      <li>Menopause</li>
    </ul>
    <p class="line centered front-address">418 Birchmont Road, Birchmont NY 11090</p>
    <p class="line centered front-contact"><span>PH: 516.555.0167/0192</span><span>FX: 516.555.0134</span><span>m-hollis@maildesk.net</span></p>
  </section>

  <section class="card card--back card--lilac" aria-label="Business card back, lilac">
    <h2 class="line centered back-name">Marvia Quenby-Hollis, MD</h2>
    <p class="line centered back-cert">Board Certified</p>
    <p class="line back-specialty"><span class="script">Women's Health &amp;</span> Wellness Specialist</p>
    <svg class="back-mark" width="80" height="80" viewBox="0 0 80 80" aria-hidden="true">
      <circle cx="40" cy="40" r="36" fill="none" stroke="var(--ink)" stroke-width="4"/>
    </svg>
    <p class="line back-service" style="top:129px;left:93px">Obstetrics</p>
    <p class="line back-service" style="top:151px;left:93px">Gynecology</p>
    <p class="line back-service" style="top:175px;left:93px">Family Planning</p>
    <p class="line back-service" style="top:199px;left:82px">Weight Managment</p>
    <p class="line back-service" style="top:222px;left:62px">Menopause</p>
    <p class="line back-detail" style="top:175px">204-15 Fernbrook Parkway</p>
    <p class="line back-detail" style="top:199px">Fernbrook, New York 11430</p>
    <p class="line back-phone" style="top:229px">(PH) 718.555.0142</p>
    <p class="line back-phone" style="top:258px">(FX) 718.555.0189</p>
    <p class="line back-email" style="top:285px">(Email) m-hollis@maildesk.net</p>
    <p class="line back-appointment">By APPOINTMENT</p>
  </section>

  <section class="card card--front card--pink" aria-label="Business card front, pink">
    <h1 class="line centered front-name">Marvia Quenby-Hollis MD</h1>
    <p class="line centered front-cert">Board Certified</p>
    <p class="line centered front-specialty">Women's Health &amp; Wellness Specialist</p>
    <p class="line front-appointment">By Appointment</p>
    <svg class="front-mark" width="116" height="100" viewBox="0 0 116 100" aria-hidden="true">
      <circle cx="58" cy="62" r="37" fill="var(--circle-gold)"/>
    </svg>
    <ul class="front-services">
      <li>Obstetrics</li>
      <li>Gynecology</li>
      <li>Family Planning</li>
      <li>Menopause</li>
    </ul>
    <p class="line centered front-address">418 Birchmont Road, Birchmont NY 11090</p>
    <p class="line centered front-contact"><span>PH: 516.555.0167/0192</span><span>FX: 516.555.0134</span><span>m-hollis@maildesk.net</span></p>
  </section>

  <section class="card card--back card--pink" aria-label="Business card back, pink">
    <h2 class="line centered back-name">Marvia Quenby-Hollis, MD</h2>
    <p class="line centered back-cert">Board Certified</p>
    <p class="line back-specialty"><span class="script">Women's Health &amp;</span> Wellness Specialist</p>
    <svg class="back-mark" width="80" height="80" viewBox="0 0 80 80" aria-hidden="true">
      <circle cx="40" cy="40" r="36" fill="none" stroke="var(--ink)" stroke-width="4"/>
    </svg>
    <p class="line back-service" style="top:129px;left:93px">Obstetrics</p>
    <p class="line back-service" style="top:151px;left:93px">Gynecology</p>
    <p class="line back-service" style="top:175px;left:93px">Family Planning</p>
    <p class="line back-service" style="top:199px;left:82px">Weight Managment</p>
    <p class="line back-service" style="top:222px;left:62px">Menopause</p>
    <p class="line back-detail" style="top:175px">204-15 Fernbrook Parkway</p>
    <p class="line back-detail" style="top:199px">Fernbrook, New York 11430</p>
    <p class="line back-phone" style="top:229px">(PH) 718.555.0142</p>
    <p class="line back-phone" style="top:258px">(FX) 718.555.0189</p>
    <p class="line back-email" style="top:285px">(Email) m-hollis@maildesk.net</p>
    <p class="line back-appointment">By APPOINTMENT</p>
  </section>

</main>
</body>
</html>
```